Develop a PowerPoint template based on existing logo for a non-profit international alliance of professionals.
Presentations that will be made with this template will include mostly bullet point text and some tables. SOme images could also be included.

Target Market(s)

Governments, private funders

Industry/Entity Type

Non-Profit

Requirements
Must have
• clean and modern feel
Should not have
• no background in the slide area

```html
<!DOCTYPE html>
<html lang="en">
<head>
<meta charset="utf-8">
<title>GVA Presentation Template</title>
<link rel="stylesheet" href="https://fonts.googleapis.com/css2?family=Jost:wght@300;400;500;700&display=swap">
<style>
  :root {
    --stage: #e4e4e4;
    --red-top: #cc0009;
    --red-mid: #a60008;
    --red-deep: #560000;
    --band: #000000;
    --white: #ffffff;
    --ink: #111111;
    --brand: #d0121b;
    --arc-shade: #c9c9c9;
    --koala-tone: #8d8a82;
    --desert-tone: #b4552a;
  }
  html, body {
    margin: 0;
    width: 1200px;
    height: 900px;
    overflow: hidden;
    background: var(--stage);
    font-family: "Jost", "Futura", sans-serif;
  }
  .canvas { position: relative; width: 1200px; height: 900px; }

  .slide {
    position: absolute;
    width: 496px;
    height: 372px;
    overflow: hidden;
  }
  .slide--content-red { left: 645px; top: 37px; }
  .slide--content-white { left: 357px; top: 260px; }
  .slide--title { left: 46px; top: 475px; }

  .slide--red {
    background: linear-gradient(180deg, var(--red-top) 0%, var(--red-top) 25%, var(--red-mid) 55%, var(--red-deep) 92%);
  }
  .slide--white { background: var(--white); }

  .slide__arc { position: absolute; left: 0; top: 0; width: 496px; height: 72px; }

  .brand {
    position: absolute;
    top: 22px;
    left: 0;
    width: 100%;
    display: flex;
    justify-content: center;
    align-items: center;
    gap: 6px;
    color: var(--brand);
    font-weight: 500;
    font-size: 12px;
    letter-spacing: 0.2px;
  }
  .brand__dot { width: 13px; height: 13px; border-radius: 50%; background: var(--brand); }

  .slide__band {
    position: absolute; left: 0; bottom: 0; width: 100%; height: 30px; background: var(--band);
  }

  .slide__rule { position: absolute; left: 50px; top: 25px; width: 2px; height: 83px; }
  .slide--red .slide__rule { background: var(--band); }
  .slide--white .slide__rule { background: var(--brand); top: 30px; height: 76px; left: 52px; }

  .slide__heading {
    position: absolute; left: 69px; top: 91px; margin: 0;
    font-size: 15px; font-weight: 700; letter-spacing: 0.2px;
  }
  .slide--red .slide__heading { color: var(--white); }
  .slide--white .slide__heading { color: var(--ink); }

  .slide__body {
    position: absolute; left: 69px; top: 125px; width: 340px; margin: 0;
    font-size: 10.5px; font-weight: 300; line-height: 13.5px;
  }
  .slide--red .slide__body { color: var(--white); }
  .slide--white .slide__body { color: var(--ink); width: 300px; top: 126px; }

  .slide__bullets {
    position: absolute; left: 69px; top: 176px; margin: 0; padding: 0 0 0 19px;
    width: 360px; color: var(--white); font-size: 10.5px; font-weight: 300; line-height: 13.5px;
  }
  .slide__bullets li { margin-bottom: 12px; }

  .pattern-area { position: absolute; }
  .pattern-area--faint-red {
    left: 350px; top: 210px; width: 170px; height: 150px;
    background: radial-gradient(ellipse at 60% 55%, rgba(90,0,0,0.45), rgba(90,0,0,0) 70%);
  }
  .pattern-area--faint-grey {
    left: 360px; top: 222px; width: 150px; height: 125px;
    background: radial-gradient(ellipse at 65% 55%, rgba(200,200,200,0.7), rgba(200,200,200,0) 72%);
  }
  .pattern-area--dark-dots {
    left: 100px; top: 40px; width: 360px; height: 300px;
    background: radial-gradient(ellipse at 55% 45%, rgba(110,0,0,0.55), rgba(110,0,0,0) 68%);
  }
  .pattern-area--white-dots {
    left: 352px; top: 112px; width: 144px; height: 230px;
    background: radial-gradient(ellipse at 70% 50%, rgba(255,255,255,0.92), rgba(255,255,255,0.35) 60%, rgba(255,255,255,0) 85%);
  }

  .photo { position: absolute; top: 196px; width: 141px; height: 106px; }
  .photo--koala { left: 137px; background: linear-gradient(160deg, #6f6b5e, var(--koala-tone) 55%, #4a463d); }
  .photo--desert { left: 285px; background: linear-gradient(180deg, #5b7fb8 0%, #c38a5a 45%, var(--desert-tone) 70%, #7a3013 100%); }

  .title-block { position: absolute; left: 48px; top: 150px; color: var(--white); }
  .title-block__title { margin: 0; font-size: 28px; font-weight: 500; line-height: 34px; }
  .title-block__subtitle { margin: 0; font-size: 20px; font-weight: 300; line-height: 24px; }
</style>
</head>
<body>
<main class="canvas">

  <section class="slide slide--red slide--content-red">
    <div class="pattern-area pattern-area--faint-red" role="img" aria-label="Faint dot pattern"></div>
    <svg class="slide__arc" viewBox="0 0 496 72" aria-hidden="true">
      <path d="M0 0 Q248 130 496 0 Z" fill="var(--arc-shade)"/>
      <path d="M0 0 Q248 124 496 0 Z" fill="var(--white)"/>
    </svg>
    <div class="brand"><span class="brand__dot"></span>Global Venture Alliance</div>
    <div class="slide__rule"></div>
    <h2 class="slide__heading">Lorem ipsum dolor sit amet</h2>
    <p class="slide__body">Lorem ipsum dolor sit amet, consectetuer adipiscing elit. Nam nibh. Nunc varius facilisis eros. Sed erat. In in velit quis arcu ornare laoreet. Curabitur adipiscing luctus massa.</p>
    <ul class="slide__bullets">
      <li>Integer ut purus ac augue commodo commodo.</li>
      <li>Nunc nec mi eu justo tempor consectetuer. Etiam vitae nisl. In dignissim lacus ut ante.</li>
      <li>Cras elit lectus, bibendum a, adipiscing vitae, commodo et, dui.</li>
    </ul>
    <div class="slide__band"></div>
  </section>

  <section class="slide slide--white slide--content-white">
    <div class="pattern-area pattern-area--faint-grey" role="img" aria-label="Faint grey dot pattern"></div>
    <svg class="slide__arc" viewBox="0 0 496 72" aria-hidden="true">
      <path d="M0 0 Q248 130 496 0" fill="none" stroke="var(--arc-shade)" stroke-width="3"/>
      <path d="M0 0 Q248 124 496 0 Z" fill="var(--white)"/>
    </svg>
    <div class="brand"><span class="brand__dot"></span>Global Venture Alliance</div>
    <div class="slide__rule"></div>
    <h2 class="slide__heading">Lorem ipsum dolor sit amet</h2>
    <p class="slide__body">Etiam vitae nisl. In dignissim lacus ut ante. Cras elit lectus, bibendum a, adipiscing vitae, commodo et, dui.</p>
    <div class="photo photo--koala" role="img" aria-label="Photo of a koala"></div>
    <div class="photo photo--desert" role="img" aria-label="Photo of a red desert butte at sunset"></div>
    <div class="slide__band"></div>
  </section>

  <section class="slide slide--red slide--title">
    <div class="pattern-area pattern-area--dark-dots" role="img" aria-label="Dark red dot pattern"></div>
    <div class="pattern-area pattern-area--white-dots" role="img" aria-label="White dot pattern"></div>
    <svg class="slide__arc" viewBox="0 0 496 72" aria-hidden="true">
      <path d="M0 0 Q248 130 496 0 Z" fill="var(--arc-shade)"/>
      <path d="M0 0 Q248 124 496 0 Z" fill="var(--white)"/>
    </svg>
    <div class="brand"><span class="brand__dot"></span>Global Venture Alliance</div>
    <div class="title-block">
      <h1 class="title-block__title">Powerpoint Title</h1>
      <p class="title-block__subtitle">Powerpoint Subtitle</p>
    </div>
    <div class="slide__band"></div>
  </section>

</main>
</body>
</html>
```